Label to go onto food packaging.

We need to create a visually interesting and appealing label to stick onto our take away food packaging. The label should contain information of the food products our cafe sells. The label is to go onto biodegradable food bowls and clam shell packaging.
The information is basically the lines we sell - buddha bowls, super smoothies, vegan burgers and curries. And also the slogan 'nourish and refresh'. We have a logo design that we would like to incorporate onto the label (but not essential)
The design will go onto a rectangle strip label.
The colours of our food outlet are splashes of yellow, blue and grey in a white interior.
We also feature a large garden green wall. You may view images from our instagram page quiet pebble kitchen

Target Market(s)

Young professional, health conscious, plant based eaters. To be used on takeaway packaging.

Industry/Entity Type

Food Production

Font styles to use
Sans Serif

Colors

Designer to choose colors to be used in the design.

Requirements
Must have
• Bold, appealing, informative.
Nice to have
• Logo incorporated, possibly as a watermark?
Should not have
• No floral shapes. If incorporating the logo, use a circle or nothing around it. No pictures/photos of food

```html
<!DOCTYPE html>
<html lang="en">
<head>
<meta charset="utf-8">
<title>quiet pebble kitchen – takeaway label</title>
<link rel="stylesheet" href="https://fonts.googleapis.com/css2?family=Nunito:wght@800;900&display=swap">
<style>
  :root {
    --label-blue: #0098da;
    --label-yellow: #fff100;
    --label-white: #ffffff;
    --pill-radius: 12px;
  }
  * { margin: 0; padding: 0; box-sizing: border-box; }
  html, body {
    width: 1200px;
    height: 320px;
    overflow: hidden;
    background: var(--label-blue);
  }
  .label {
    position: relative;
    width: 1200px;
    height: 320px;
    background: var(--label-blue);
    font-family: "Nunito", Arial, sans-serif;
  }
  .label__panel {
    position: absolute;
    left: 20px;
    top: 20px;
    width: 1160px;
    height: 278px;
    border-radius: 36px;
    background: var(--label-yellow);
  }
  .pill {
    position: absolute;
    display: flex;
    align-items: center;
    justify-content: center;
    background: var(--label-blue);
    border-radius: var(--pill-radius);
    color: var(--label-white);
    font-weight: 900;
    letter-spacing: -0.3px;
    white-space: nowrap;
    -webkit-text-stroke: 1px var(--label-blue);
    text-shadow: 0 0 1px rgba(0, 80, 130, 0.6);
  }
  .pill--slogan {
    left: 36px; top: 34px; width: 402px; height: 60px;
    border-radius: 16px;
    font-size: 40px;
  }
  .pill--line {
    width: 268px; height: 42px;
    font-size: 27px;
  }
  .pill--bowls     { left: 346px; top: 102px; }
  .pill--smoothies { left: 521px; top: 152px; }
  .pill--burgers   { left: 696px; top: 202px; height: 43px; }
  .pill--curries   { left: 872px; top: 253px; }

  .brand {
    position: absolute;
    left: 966px;
    top: 24px;
    width: 200px;
    height: 200px;
    border: 4px solid var(--label-blue);
    border-radius: 50%;
    display: flex;
    align-items: center;
    justify-content: center;
    text-align: center;
    color: var(--label-blue);
    font-weight: 900;
    font-size: 22px;
    line-height: 1.05;
    text-transform: uppercase;
  }
</style>
</head>
<body>
  <main class="label">
    <div class="label__panel" role="img" aria-label="Yellow background with a repeating pattern of small white sunbursts"></div>

    <h1 class="pill pill--slogan">Nourish &amp; Refresh</h1>

    <ul class="menu-lines" aria-label="Menu lines">
      <li class="pill pill--line pill--bowls">Buddha Bowls</li>
      <li class="pill pill--line pill--smoothies">Super Smoothies</li>
      <li class="pill pill--line pill--burgers">Vegan Burgers</li>
      <li class="pill pill--line pill--curries">Curries</li>
    </ul>

    <div class="brand">quiet<br>pebble<br>kitchen</div>
  </main>
</body>
</html>
```